Book Cover needs A GREAT Design

I need a book cover designed for my book "Quiet Harbors, Waking to Bloom,
subtitle "Reading the Grammar of Night Visions", by Marion Vaughtley. The book cover needs to reflect the inner contents of the book which is how to understand the symbolic transformational images within our dreams.

Dreams speak to us in a rich visual vocabulary. We dreamed before we had a written language. I want a book cover that uses imagery to draw the reader into the book.

In the language of dreams whenever death occurs it symbolizes a profound pyschological transformation. My clients are all ages 18 to 88+, I want a cover that engages people's unconscious knowing when they look at it. Book Cover formatted to 8.5" x 5.5" I need a high resolution cover, minimum 300dpi so that the cover prints well.

Please save a space for the ISBN Number. The book will be 150-200 pages.
I have attached a photo of myself, for a small picture of me on the back cover. Book will be about 150 pages. Thanks.
Updates

 Author name on the cover: Marion Vaughtley

Reason: I am extending the deadline for 7 days. I have had my own deadline for a project which is tomorrow, so I cannot do anything else unitl that Report is complete. Thank you, Marion

Thank you all for your submissions. I extended the deadline so that I can deal with a report that I have to have done by tomorrow. So book cover has been on the back burner.

Target Market(s)

Any one who wants to gain greater understanding from their dreams. My clients are mostly 18 to 88, I developed the BRIDGE™ Method to help people interpret their dreams, run Dream Groups and Workshops with Art from Dreams. I focus on the holistic, integrative health and wholeness of body mind, and spirit shown in dreams. Especially physical health.

Colors
f04a50
e567a6
a54599
0692cc
ec1f27
3276b5

Requirements
Must have
• I want the cover to be bright vibrant colors peachy pinks, a bit of purplish magenta, and perhaps turquoise blue. I want a transformational image on the front, like a phoenix rising from the ashes. I do not want a stark photographic look. The image must have a dream like quality. I would like the main part of the title font to be a bit shadowed, and I am open to creative suggestions. Document attached has colors I like. I like the idea of shadowed or reflective font because so much of our psyche hides in the "shadows".
Nice to have
• I really want to focus on a transformational image, to emphasize how dreams come with transformational information for our psyche.
Should not have
• No stark, real photographic images for cover. No dark colors. Nothing neon or sci-fi looking. No business like fonts like Times New Roman.

```html
<!DOCTYPE html>
<html lang="en">
<head>
<meta charset="UTF-8">
<title>Quiet Harbors, Waking to Bloom — Book Cover</title>
<link href="https://fonts.googleapis.com/css2?family=Cinzel:wght@700&family=Cormorant+Garamond:wght@500;600&display=swap" rel="stylesheet">
<style>
  :root {
    --canvas: #ffffff;
    --violet-deep: #5b2d91;
    --violet: #8a5cb8;
    --lilac: #cdb6e0;
    --mist: #f3ecf7;
    --flame-pink: #e567a6;
    --flame-red: #ec1f27;
    --flame-gold: #f7c548;
    --turquoise: #8fd3e8;
    --title-ink: #5e2a8f;
    --subtitle-ink: #ec3a2f;
    --author-ink: #ffffff;
    --band: rgba(255, 255, 255, 0.78);
  }
  * { margin: 0; padding: 0; box-sizing: border-box; }
  html, body {
    width: 1200px;
    height: 912px;
    overflow: hidden;
    background: var(--canvas);
  }
  .canvas {
    position: relative;
    width: 1200px;
    height: 912px;
    background: var(--canvas);
  }
  .cover {
    position: absolute;
    left: 330px;
    top: 55px;
    width: 534px;
    height: 819px;
    overflow: hidden;
  }
  .cover-art {
    position: absolute;
    inset: 0;
    background:
      radial-gradient(ellipse 22% 20% at 50% 36%, var(--flame-gold) 0%, var(--flame-red) 35%, var(--flame-pink) 60%, transparent 100%),
      radial-gradient(ellipse 12% 14% at 50% 66%, var(--flame-gold) 0%, transparent 100%),
      radial-gradient(ellipse 40% 8% at 50% 95%, var(--turquoise) 0%, #f6cde4 50%, transparent 100%),
      linear-gradient(60deg, transparent 30%, var(--violet) 45%, transparent 60%),
      linear-gradient(-60deg, transparent 30%, var(--violet) 45%, transparent 60%),
      radial-gradient(ellipse 40% 35% at 50% 5%, #ffffff 0%, var(--mist) 50%, transparent 100%),
      linear-gradient(180deg, var(--lilac) 0%, #b79ad6 50%, #d8c3e6 85%, #f3d9ec 100%);
  }
  .title-band {
    position: absolute;
    left: 0;
    top: 356px;
    width: 100%;
    height: 166px;
    background: var(--band);
    text-align: center;
    padding-top: 18px;
  }
  .title {
    font-family: "Cormorant Garamond", Georgia, serif;
    font-weight: 600;
    font-size: 41px;
    line-height: 44px;
    color: var(--title-ink);
    text-shadow: 1px 2px 2px rgba(94, 42, 143, 0.3);
  }
  .subtitle {
    margin-top: 10px;
    font-family: "Cinzel", Georgia, serif;
    font-weight: 700;
    font-size: 16px;
    letter-spacing: 0.3px;
    color: var(--subtitle-ink);
  }
  .author {
    position: absolute;
    left: 0;
    top: 672px;
    width: 100%;
    text-align: center;
    font-family: "Cinzel", Georgia, serif;
    font-weight: 700;
    font-size: 33px;
    letter-spacing: 0.5px;
    color: var(--author-ink);
    text-shadow: 0 2px 6px rgba(70, 30, 110, 0.6);
  }
</style>
</head>
<body>
  <div class="canvas">
    <div class="cover">
      <div class="cover-art" role="img" aria-label="Dreamlike painted phoenix with fiery pink, red and gold wings rising through soft purple light and sparkles"></div>
      <div class="title-band">
        <h1 class="title">Quiet Harbors,<br>Waking to Bloom</h1>
        <p class="subtitle">Reading the Grammar of Night Visions</p>
      </div>
      <p class="author">Marion Vaughtley</p>
    </div>
  </div>
</body>
</html>
```